Frostwyn.co - Polar Expeditions Specialists

We need a modern, visually striking business card for Frostwyn.co, a company specialized in selling expedition cruises to the most remote regions on Earth, with a focus on the Arctic and Antarctica. The design should instantly communicate that the cardholder is an expert in polar travel. Use clean, premium aesthetics with cool tones like icy blue and white, possibly incorporating polar imagery (ice, glaciers, penguins, etc.)

Attached the logo

Contact Information for Business Card

Feels high-end and trustworthy.. Visually memorable — encourages people to keep it

Colors
0054AA
0677BA
7BADD7
CADEEF
E8F1F8

Requirements
Must have
• ice, glaciers, penguins, montains
Nice to have
• modern, transparente,

```html
<!DOCTYPE html>
<html lang="en">
<head>
<meta charset="UTF-8">
<title>Frostwyn.co – Business Card</title>
<link rel="stylesheet" href="https://fonts.googleapis.com/css2?family=Poppins:wght@300;400;600;700&display=swap">
<style>
  :root {
    --stage: #2f3033;
    --card-navy: #1f2d52;
    --card-slate: #4a5b7c;
    --ice-light: #cadeef;
    --ice-mid: #7badd7;
    --ice-deep: #3d5173;
    --white: #ffffff;
  }
  * { margin: 0; padding: 0; box-sizing: border-box; }
  html, body {
    width: 800px; height: 1200px; overflow: hidden;
    background: var(--stage);
    font-family: "Poppins", sans-serif;
    color: var(--white);
  }
  .stage {
    width: 800px; height: 1200px;
    display: flex; flex-direction: column;
    align-items: center; justify-content: center; gap: 120px;
  }
  .card {
    position: relative;
    width: 640px; height: 366px;
    overflow: hidden;
    box-shadow: 0 12px 30px rgba(0,0,0,.45);
  }

  /* Front */
  .card--front { background: var(--card-navy); }
  .brand { position: absolute; }
  .brand--front { left: 52px; top: 88px; }
  .brand__mark {
    width: 64px; height: 64px; border-radius: 50%;
    background: var(--white);
    margin: 0 0 10px 74px;
  }
  .brand__name {
    font-weight: 700; font-size: 40px; line-height: 1; letter-spacing: -.5px;
    white-space: nowrap;
  }
  .brand__tagline {
    margin-top: 6px; font-weight: 600; font-size: 11.5px; letter-spacing: .2px;
    white-space: nowrap;
  }
  .contact {
    position: absolute; left: 372px; top: 96px;
  }
  .contact__name {
    font-weight: 700; font-size: 19px; letter-spacing: .6px; text-transform: uppercase; line-height: 1.15;
  }
  .contact__role {
    font-weight: 600; font-size: 13px; letter-spacing: .6px; text-transform: uppercase;
  }
  .contact__rule {
    width: 30px; height: 3px; background: var(--white); margin: 16px 0;
  }
  .contact__lines {
    font-weight: 300; font-size: 15px; line-height: 1.35; letter-spacing: .3px;
  }
  .contact__lines + .contact__lines { margin-top: 12px; }

  /* Back */
  .card--back { background: var(--card-slate); }
  .glacier-scene {
    position: absolute; left: 0; right: 0; bottom: 0; height: 200px;
    background: linear-gradient(180deg, rgba(202,222,239,0) 0%, rgba(202,222,239,.3) 30%, var(--ice-deep) 100%);
  }
  .glacier-feature {
    position: absolute; left: 64px; top: 64px; width: 220px; height: 290px;
    border-radius: 46% 54% 10% 10% / 38% 40% 8% 8%;
    background: linear-gradient(180deg, var(--ice-light) 0%, #a9bfd6 45%, #56688a 100%);
    opacity: .9;
  }
  .brand--back { left: 316px; top: 206px; }
  .brand--back .brand__name { font-size: 46px; }
  .brand--back .brand__tagline { font-size: 13px; }
</style>
</head>
<body>
<main class="stage">
  <section class="card card--front">
    <div class="brand brand--front">
      <div class="brand__mark"></div>
      <div class="brand__name">Frostwyn.co</div>
      <div class="brand__tagline">Polar Expeditions Specialists</div>
    </div>
    <div class="contact">
      <div class="contact__name">Marcus Hallberg</div>
      <div class="contact__role">Managing Director</div>
      <div class="contact__rule"></div>
      <p class="contact__lines">P 555 010 22 84<br>E info@frostwyn.co</p>
      <p class="contact__lines">48 Harbor Lane<br>Northport, Maine 04849</p>
    </div>
  </section>

  <section class="card card--back">
    <div class="glacier-scene" role="img" aria-label="Photograph of icebergs floating in calm polar water"></div>
    <div class="glacier-feature" role="img" aria-label="Large glacier ice formation image"></div>
    <div class="brand brand--back">
      <div class="brand__name">Frostwyn.co</div>
      <div class="brand__tagline">Polar Expeditions Specialists</div>
    </div>
  </section>
</main>
</body>
</html>
```